Elegant One-Page Flyer That Catches People's Eye

For a series of workshops and zoom calls I am marketing with a colleague of mine, we would like to have an elegant, catchy one-page flyer that entices people to contact us. I am envisioning a one-page flyer (a card that is somewhat larger than a postcard) with great text, layout and images which magnetically draws people to us and is positive and inspiring. Also, if at all possible, a QR code linking it to our websites. Good colours would be shades of blue and green. I am uploading: the Text, our pictures, logos and contact information.

```html
<!DOCTYPE html>
<html lang="en">
<head>
<meta charset="utf-8">
<title>Rising above Hidden Career Deal Breakers – Workshop Flyer</title>
<link href="https://fonts.googleapis.com/css2?family=Montserrat:wght@400;500;600;700&display=swap" rel="stylesheet">
<style>
  :root {
    --stage: #cfd0d0;
    --paper: #f0f2f3;
    --paper-white: #ffffff;
    --green: #8ab857;
    --maroon: #5a1a1f;
    --ink: #1d1d1d;
    --rule: #7d7d7d;
    --sky-1: #2f6fb3;
    --sky-2: #d9e6f2;
  }
  * { margin: 0; padding: 0; box-sizing: border-box; }
  html, body { width: 1200px; height: 2340px; overflow: hidden; }
  body { background: var(--stage); font-family: "Montserrat", sans-serif; color: var(--ink); position: relative; }

  .flyer { position: absolute; left: 50px; top: 392px; width: 1100px; height: 1556px; background: var(--paper); overflow: hidden; }
  .flyer-shapes { position: absolute; left: 0; top: 0; width: 1100px; height: 1556px; }
  .abs { position: absolute; }

  .brand { top: 58px; display: flex; align-items: center; gap: 10px; font-weight: 500; font-size: 34px; letter-spacing: 0.5px; }
  .brand-primary { left: 40px; color: var(--green); }
  .brand-dot { width: 36px; height: 36px; border-radius: 50%; border: 3px solid var(--green); }
  .brand-divider { left: 336px; top: 56px; width: 2px; height: 52px; background: var(--maroon); }
  .brand-partner { left: 363px; top: 50px; color: var(--maroon); font-size: 30px; font-weight: 500; }
  .brand-partner-city { left: 560px; top: 90px; color: var(--maroon); font-size: 16px; font-weight: 500; }

  .hook { left: 40px; font-size: 35px; font-weight: 600; line-height: 40px; }
  .hook-light { color: var(--paper-white); }
  .hook-dark { color: var(--ink); }
  .hook-rule { left: 40px; width: 456px; height: 2px; background: var(--ink); opacity: .55; }

  .intro { left: 40px; top: 577px; font-size: 26px; font-weight: 600; line-height: 31px; width: 470px; }
  .benefits { left: 40px; top: 700px; list-style: none; font-size: 22px; line-height: 24px; width: 470px; }
  .benefits li { display: flex; align-items: center; gap: 14px; margin-bottom: 16px; }
  .benefits svg { flex: none; }

  .col-rule { width: 2px; background: var(--rule); opacity: .6; }

  .offer-title { left: 590px; top: 658px; font-size: 29px; font-weight: 600; line-height: 36px; }
  .badge { background: var(--maroon); color: var(--paper-white); font-weight: 600; border-radius: 6px; padding: 2px 12px; }
  .format-badge { left: 590px; top: 756px; font-size: 26px; }
  .format-text { left: 590px; top: 812px; font-size: 22px; line-height: 27px; width: 420px; }
  .format-text strong { font-weight: 600; }

  .facilitators-badge { left: 40px; top: 967px; font-size: 25px; }
  .facilitator-name { left: 40px; font-size: 21px; font-weight: 700; }
  .facilitator-bio { left: 40px; font-size: 18.5px; line-height: 24px; width: 340px; font-weight: 500; }
  .portrait { left: 405px; width: 145px; height: 182px; border-radius: 8px; border: 3px solid var(--paper-white); }
  .portrait-warm { background: linear-gradient(160deg, #a5492c 0%, #c98a5a 45%, #8e79b5 100%); }
  .portrait-light { background: linear-gradient(180deg, #f4f4f4 0%, #e5e5e5 60%, #1b1b1b 100%); }
  .facilitator-rule { left: 40px; top: 1272px; width: 1020px; height: 2px; background: var(--rule); opacity: .6; }

  .contact-box { left: 590px; top: 927px; width: 510px; height: 119px; background: var(--green); border-radius: 8px 0 0 0; padding: 40px 0 0 40px; color: var(--ink); }
  .contact-box p { font-size: 18px; line-height: 24px; }
  .contact-box strong { font-size: 21px; font-weight: 700; }

  .contact-list { left: 630px; list-style: none; font-size: 23px; }
  .contact-list li { display: flex; align-items: center; gap: 14px; height: 42px; }
  .contact-list .who, .contact-list .phone { font-weight: 700; }
  .contact-list b { font-weight: 700; }
</style>
</head>
<body>
<main class="flyer">
  <svg class="flyer-shapes" viewBox="0 0 1100 1556" preserveAspectRatio="none" aria-hidden="true">
    <rect x="0" y="544" width="1100" height="383" fill="var(--paper-white)"/>
    <rect x="0" y="544" width="550" height="383" fill="var(--paper-white)"/>
    <defs>
      <linearGradient id="sky" x1="0" y1="0" x2="0.4" y2="1">
        <stop offset="0" stop-color="var(--sky-1)"/>
        <stop offset="0.55" stop-color="var(--sky-2)"/>
        <stop offset="1" stop-color="#5d6a77"/>
      </linearGradient>
    </defs>
    <polygon points="750,0 1100,0 1100,623 532,623 362,544" fill="url(#sky)" role="img" aria-label="Photo of a climber in a red jacket hanging from a rope under a rock overhang against a blue cloudy sky"/>
    <polygon points="0,167 629,167 357,544 0,544" fill="var(--green)"/>
    <polygon points="357,544 508,544 429,457" fill="var(--maroon)"/>
    <rect x="0" y="1516" width="590" height="40" fill="var(--green)"/>
    <polygon points="590,1516 1100,1516 1100,1556 590,1556" fill="var(--maroon)"/>
  </svg>

  <div class="abs brand brand-primary"><span class="brand-dot"></span>PathWise</div>
  <div class="abs brand-divider"></div>
  <div class="abs brand-partner">Keller Coaching</div>
  <div class="abs brand-partner-city">Zürich</div>

  <h2 class="abs hook hook-light" style="top:200px">Is your career going<br>the way you want?</h2>
  <div class="abs hook-rule" style="top:299px"></div>
  <h2 class="abs hook hook-dark" style="top:314px">If not, do you feel stuck?<br>Blocked? Frustrated?</h2>
  <div class="abs hook-rule" style="top:411px"></div>
  <h2 class="abs hook hook-light" style="top:430px">Don’t know what to<br>do about this?</h2>

  <p class="abs intro">Learn to overcome and rise above the 4 top hidden career deal breakers fast:</p>
  <ul class="abs benefits">
    <li><svg width="26" height="26" viewBox="0 0 26 26"><circle cx="13" cy="13" r="13" fill="var(--green)"/><path d="M7 13.5l4 4 8-8" stroke="#fff" stroke-width="2.6" fill="none" stroke-linecap="round" stroke-linejoin="round"/></svg>Microaggressions</li>
    <li><svg width="26" height="26" viewBox="0 0 26 26"><circle cx="13" cy="13" r="13" fill="var(--green)"/><path d="M7 13.5l4 4 8-8" stroke="#fff" stroke-width="2.6" fill="none" stroke-linecap="round" stroke-linejoin="round"/></svg>Toxic black box team dynamics</li>
    <li><svg width="26" height="26" viewBox="0 0 26 26"><circle cx="13" cy="13" r="13" fill="var(--green)"/><path d="M7 13.5l4 4 8-8" stroke="#fff" stroke-width="2.6" fill="none" stroke-linecap="round" stroke-linejoin="round"/></svg><span>Workplace snakes and other<br>dysfunctional types</span></li>
    <li><svg width="26" height="26" viewBox="0 0 26 26"><circle cx="13" cy="13" r="13" fill="var(--green)"/><path d="M7 13.5l4 4 8-8" stroke="#fff" stroke-width="2.6" fill="none" stroke-linecap="round" stroke-linejoin="round"/></svg><span>Disempowering Subconscious<br>Algorithms</span></li>
  </ul>

  <div class="abs col-rule" style="left:550px;top:665px;height:220px"></div>

  <h2 class="abs offer-title">Rising above Hidden Career<br>Deal breakers</h2>
  <div class="abs badge format-badge">Format:</div>
  <p class="abs format-text"><strong>4 Mini-Workshops + 2 short Online Group Coaching</strong> Sessions between Workshops</p>

  <div class="abs badge facilitators-badge">Facilitators</div>

  <h3 class="abs facilitator-name" style="top:1040px">Dr. Mara Ellwood,</h3>
  <p class="abs facilitator-bio" style="top:1086px">PhD, CPC, is an American and Swiss-Trained Work and Organizational Psychologist, ICF-Certified Coach, Board Certified Hypnotherapist, Certified Naturopath (TEN) and Certified Ayurvedic Practitioner.</p>
  <div class="abs portrait portrait-warm" style="top:1058px" role="img" aria-label="Portrait photo of Dr. Mara Ellwood"></div>

  <div class="abs facilitator-rule"></div>

  <h3 class="abs facilitator-name" style="top:1312px">Dr. Nora Keller,</h3>
  <p class="abs facilitator-bio" style="top:1358px">Ph.D., PCC is a coach &amp; somatic experience practitioner, a team coach with diploma &amp; a certified virtual team coach.</p>
  <div class="abs portrait portrait-light" style="top:1292px" role="img" aria-label="Portrait photo of Dr. Nora Keller"></div>

  <div class="abs contact-box">
    <p>For dates, venue and further information</p>
    <strong>Contact Nora / Mara at:</strong>
  </div>

  <div class="abs col-rule" style="left:590px;top:1090px;height:113px"></div>
  <ul class="abs contact-list" style="top:1076px">
    <li><svg width="28" height="28" viewBox="0 0 28 28"><circle cx="14" cy="14" r="14" fill="var(--maroon)"/><circle cx="14" cy="11" r="3.5" fill="none" stroke="#fff" stroke-width="1.8"/><path d="M8 20c1-3.5 11-3.5 12 0z" fill="none" stroke="#fff" stroke-width="1.8" stroke-linejoin="round"/></svg><span class="who">Mara</span></li>
    <li><svg width="28" height="28" viewBox="0 0 28 28"><circle cx="14" cy="14" r="14" fill="var(--maroon)"/><rect x="7.5" y="9" width="13" height="10" rx="1.5" fill="none" stroke="#fff" stroke-width="1.8"/><path d="M8 10l6 5 6-5" fill="none" stroke="#fff" stroke-width="1.8"/></svg><span>mara@<b>pathwise</b>.ch</span></li>
    <li><svg width="28" height="28" viewBox="0 0 28 28"><circle cx="14" cy="14" r="14" fill="var(--green)"/><path d="M10 8l2.5 0 1.2 3.2-1.6 1.2c.8 1.7 1.8 2.7 3.5 3.5l1.2-1.6 3.2 1.2 0 2.5c-6 .5-10.5-4-10-10z" fill="#fff"/></svg><span class="phone">076 000 12 34</span></li>
  </ul>

  <div class="abs col-rule" style="left:590px;top:1323px;height:113px"></div>
  <ul class="abs contact-list" style="top:1309px">
    <li><svg width="28" height="28" viewBox="0 0 28 28"><circle cx="14" cy="14" r="14" fill="var(--maroon)"/><circle cx="14" cy="11" r="3.5" fill="none" stroke="#fff" stroke-width="1.8"/><path d="M8 20c1-3.5 11-3.5 12 0z" fill="none" stroke="#fff" stroke-width="1.8" stroke-linejoin="round"/></svg><span class="who">Nora</span></li>
    <li><svg width="28" height="28" viewBox="0 0 28 28"><circle cx="14" cy="14" r="14" fill="var(--maroon)"/><rect x="7.5" y="9" width="13" height="10" rx="1.5" fill="none" stroke="#fff" stroke-width="1.8"/><path d="M8 10l6 5 6-5" fill="none" stroke="#fff" stroke-width="1.8"/></svg><span>nora@<b>kellercoaching</b>.ch</span></li>
    <li><svg width="28" height="28" viewBox="0 0 28 28"><circle cx="14" cy="14" r="14" fill="var(--green)"/><path d="M10 8l2.5 0 1.2 3.2-1.6 1.2c.8 1.7 1.8 2.7 3.5 3.5l1.2-1.6 3.2 1.2 0 2.5c-6 .5-10.5-4-10-10z" fill="#fff"/></svg><span class="phone">079 000 56 78</span></li>
  </ul>
</main>
</body>
</html>
```